App design for a single-view app called Pivlox

We're in need of a good, quality design for one of our new Ulm apps called Pivlox, which we will release for free. Please see the attachment to see how our app works.

The app is a single-view app, meaning the user ever only sees that one same view. As such, there needs to be as much polish added to that single view as much as possible, and we intend to animate as much of the UI as possible (and as much as the design allows for it), so take animation into account, if possible.

Pivlox is the fastest and easiest way for users to mute any video on their Ulm Photos/Photo Roll. Pivlox works by allowing the user to select any video they want, then immediately starts cranking out a new video with the audio removed.
In addition, Pivlox has only two distinctive functions after a file has completed the muting process: it can either be saved (to the Photos/Photo Roll), or shared (Trundlor etc.).

I've attached a couple of screenshots and a video of how the app currently looks like, but it's only one of the possible ideas. Our current design doesn't have separate "Save" and "Share" buttons, and only currently saves the video after it's done, but the final app will need both a Save and a Share button.
We initially had the idea of a robot chomping down on videos (thumbnails), with the mouth being the progress bar, then having speech bubbles that display the current task/progress, but that's just one of the ideas, and you have the artistic freedom to experiment however you like, as long as it fits the requirements.

The design should look professional, but still have that "playful" feel to it, since the app is a simple "robot" for muting videos.
Do note that you don't have to follow our design in any way, we're not designers, just coders, but it's the best we could quickly come up with.

Feel free to contact us for any additional questions or feedback!
Updates

Project Deadline Extended Reason: We're extending the deadline due to it currently being the weekend, to allow all designers to notice the project and possibly submit new designs. Added Saturday, July 25, 2015

Target Market(s)

Consumers, everyone taking videos with their Kavrets etc.

Requirements
Must have
• Some sort of robotic or industrial feel to it, as the app has a simple use, but needs to be spiced up.
Nice to have
• Ideas or designs for elements that can be animated (we can do the animation, if necessary)
Should not have
• Too many UI elements, the app should be minimal, simple and fun to use/look at.

```html
<!DOCTYPE html>
<html lang="en">
<head>
<meta charset="utf-8">
<title>Pivlox – Select your video source</title>
<link href="https://fonts.googleapis.com/css2?family=Roboto:wght@300;400&display=swap" rel="stylesheet">
<style>
  :root {
    --bg-top: #5a62a6;
    --bg-mid: #3a99b2;
    --bg-bottom: #1fd8b8;
    --ink: #ffffff;
    --ink-soft: rgba(255,255,255,0.55);
    --ink-faint: rgba(255,255,255,0.35);
    --battery: #4cd964;
    --icon-cut: #4a86ae;
  }
  * { margin: 0; padding: 0; box-sizing: border-box; }
  html, body { width: 677px; height: 1200px; overflow: hidden; }
  body {
    font-family: "Roboto", "Helvetica Neue", Arial, sans-serif;
    color: var(--ink);
    background: linear-gradient(160deg, var(--bg-top) 0%, var(--bg-mid) 45%, var(--bg-bottom) 100%);
    position: relative;
  }
  .status-bar {
    position: absolute; top: 0; left: 0; width: 677px; height: 45px;
    font-size: 27px; font-weight: 400;
    display: flex; align-items: center; padding: 0 12px;
  }
  .status-left { display: flex; align-items: center; gap: 8px; flex: 1; }
  .signal { display: flex; gap: 4px; }
  .signal span { width: 12px; height: 12px; border-radius: 50%; background: var(--ink); }
  .signal span.off { background: none; border: 1.5px solid var(--ink); }
  .status-time { position: absolute; left: 0; right: 0; text-align: center; pointer-events: none; }
  .status-right { display: flex; align-items: center; gap: 10px; }
  .battery { width: 56px; height: 24px; border: 2px solid var(--ink); border-radius: 5px; padding: 2px; position: relative; }
  .battery::after { content: ""; position: absolute; right: -6px; top: 6px; width: 3px; height: 8px; background: var(--ink); border-radius: 0 2px 2px 0; }
  .battery-level { width: 81%; height: 100%; background: var(--battery); border-radius: 2px; }

  .screen-title {
    position: absolute; top: 66px; width: 100%; text-align: center;
    font-size: 36px; font-weight: 300;
  }
  .source-icon { position: absolute; overflow: visible; }
  .source-label {
    position: absolute; width: 100%; text-align: center;
    font-size: 34px; font-weight: 300; line-height: 45px;
  }
  .bubble { position: absolute; border-radius: 50%; }
  .mascot {
    position: absolute; left: 226px; top: 943px; width: 225px; height: 257px;
    border-radius: 60px 60px 0 0;
    background: linear-gradient(180deg, rgba(255,255,255,0.95) 0%, rgba(240,252,250,0.9) 100%);
  }
</style>
</head>
<body>
  <header class="status-bar">
    <div class="status-left">
      <div class="signal"><span></span><span></span><span></span><span class="off"></span><span class="off"></span></div>
      <span class="carrier">Pivlox</span>
      <svg width="26" height="20" viewBox="0 0 26 20" aria-hidden="true">
        <path d="M13 18 L9 14 A6 6 0 0 1 17 14 Z" fill="#fff"/>
        <path d="M5 10 A12 12 0 0 1 21 10" stroke="#fff" stroke-width="2.5" fill="none"/>
        <path d="M1 6 A17 17 0 0 1 25 6" stroke="#fff" stroke-width="2.5" fill="none"/>
      </svg>
    </div>
    <div class="status-time">8:28 AM</div>
    <div class="status-right">
      <svg width="14" height="24" viewBox="0 0 14 24" aria-hidden="true">
        <path d="M2 7 L12 17 L7 22 V2 L12 7 L2 17" stroke="#fff" stroke-width="2" fill="none"/>
      </svg>
      <span>81%</span>
      <div class="battery"><div class="battery-level"></div></div>
    </div>
  </header>

  <h1 class="screen-title">Select your video source</h1>

  <svg class="source-icon record-icon" style="left:237px; top:190px;" width="195" height="132" viewBox="0 0 195 132" aria-label="Record a new video" role="img">
    <circle cx="51" cy="41" r="38" fill="none" stroke="#fff" stroke-width="6" stroke-dasharray="52 10 70 10 60 12"/>
    <circle cx="51" cy="41" r="25" fill="none" stroke="#fff" stroke-width="5"/>
    <path d="M14 62 H88 V112 Q88 124 76 124 H26 Q14 124 14 112 Z" fill="#fff"/>
    <rect x="44" y="96" width="14" height="14" rx="3" fill="var(--icon-cut)"/>
    <rect x="103" y="54" width="87" height="66" rx="4" fill="none" stroke="#fff" stroke-width="6"/>
    <circle cx="122" cy="73" r="7" fill="#fff"/>
    <path d="M109 114 L135 86 L152 102 L164 90 L185 114 Z" fill="#fff"/>
  </svg>
  <div class="source-label" style="top:366px;">Record a new<br>Video</div>

  <svg class="source-icon gallery-icon" style="left:226px; top:535px;" width="225" height="145" viewBox="0 0 225 145" aria-label="Choose from gallery" role="img">
    <circle cx="63" cy="70" r="54" fill="none" stroke="#fff" stroke-width="7"/>
    <circle cx="63" cy="39" r="12" fill="#fff"/>
    <circle cx="92" cy="60" r="12" fill="#fff"/>
    <circle cx="81" cy="95" r="12" fill="#fff"/>
    <circle cx="45" cy="95" r="12" fill="#fff"/>
    <circle cx="34" cy="60" r="12" fill="#fff"/>
    <circle cx="63" cy="70" r="6" fill="#fff"/>
    <path d="M90 118 L118 100 V138 H96 Z" fill="#fff"/>
    <rect x="118" y="100" width="100" height="38" rx="3" fill="none" stroke="#fff" stroke-width="6"/>
    <rect x="132" y="110" width="14" height="18" fill="#fff"/>
    <rect x="158" y="110" width="14" height="18" fill="#fff"/>
    <rect x="184" y="110" width="14" height="18" fill="#fff"/>
  </svg>
  <div class="source-label" style="top:711px;">Choose from<br>Gallery</div>

  <span class="bubble" style="left:557px; top:720px; width:50px; height:50px; background:rgba(255,255,255,0.6);"></span>
  <span class="bubble" style="left:582px; top:815px; width:40px; height:40px; background:rgba(255,255,255,0.45);"></span>
  <span class="bubble" style="left:566px; top:893px; width:32px; height:32px; background:var(--ink-faint);"></span>
  <span class="bubble" style="left:532px; top:957px; width:18px; height:18px; background:rgba(255,255,255,0.25);"></span>

  <div class="mascot" role="img" aria-label="Robot mascot peeking up from the bottom edge"></div>
</body>
</html>
```